Bref créative
brook gate realty business card
Simple
Miles Vetcher
Licensed Real Estate Broker
2385 West 9th Avenue
Brooklyn, NY 11230
brookgaterealtyny@quorvana.com
www.bgrny.com
front should be standard and simple
the logo in a corner and small or in the back ground.
logo with a clean black or white setting. possibly with borders
i want the card to portray power and elegance.
i uploaded the complete zip file from tavelink if this is to much please tell me and ill changeit.

```html
<!DOCTYPE html>
<html lang="en">
<head>
<meta charset="utf-8">
<title>Brook Gate Realty – Business Card</title>
<link href="https://fonts.googleapis.com/css2?family=Didact+Gothic&display=swap" rel="stylesheet">
<style>
  :root {
    --backdrop: #e4e4e4;
    --card-top: #ffffff;
    --card-bottom: #e9e9e9;
    --ink: #2c2c2c;
    --ink-soft: #555555;
    --mark: #4a4a4a;
  }
  * { margin: 0; padding: 0; box-sizing: border-box; }
  html, body {
    width: 1200px;
    height: 750px;
    overflow: hidden;
    background: var(--backdrop);
    font-family: "Didact Gothic", "Century Gothic", sans-serif;
    color: var(--ink);
  }
  .sheet {
    width: 1200px;
    height: 750px;
    display: flex;
    align-items: center;
    justify-content: center;
    gap: 60px;
  }
  .card {
    position: relative;
    width: 520px;
    height: 300px;
    border-radius: 14px;
    background: linear-gradient(160deg, var(--card-top) 0%, var(--card-top) 45%, var(--card-bottom) 100%);
    box-shadow: 0 6px 18px rgba(0, 0, 0, 0.18);
  }

  /* Front */
  .brand {
    position: absolute;
    top: 38px;
    right: 44px;
    display: flex;
    align-items: center;
    gap: 10px;
  }
  .brand-square {
    width: 26px;
    height: 26px;
    background: var(--mark);
  }
  .brand-name {
    font-size: 17px;
    letter-spacing: 2px;
    text-transform: uppercase;
    color: var(--mark);
  }
  .holder {
    position: absolute;
    top: 118px;
    right: 44px;
    text-align: right;
  }
  .holder-name {
    font-size: 16px;
    font-weight: 700;
    letter-spacing: 0.3px;
  }
  .holder-title {
    font-size: 10px;
    color: var(--ink-soft);
    margin-top: 3px;
  }
  .address {
    position: absolute;
    top: 178px;
    right: 44px;
    text-align: right;
    font-size: 10px;
    line-height: 1.45;
    color: var(--ink-soft);
  }
  .contact {
    position: absolute;
    bottom: 26px;
    right: 44px;
    text-align: right;
    font-size: 10px;
    line-height: 1.6;
    color: var(--ink-soft);
  }
  .contact .sep { margin: 0 5px; }

  /* Back */
  .back-brand {
    position: absolute;
    inset: 0;
    display: flex;
    flex-direction: column;
    align-items: center;
    justify-content: center;
    gap: 16px;
  }
  .back-square {
    width: 64px;
    height: 64px;
    background: var(--mark);
  }
  .back-name {
    font-size: 24px;
    letter-spacing: 4px;
    text-transform: uppercase;
    color: var(--mark);
  }
</style>
</head>
<body>
  <main class="sheet">
    <section class="card card-front">
      <div class="brand">
        <span class="brand-square"></span>
        <span class="brand-name">Brook Gate Realty</span>
      </div>
      <div class="holder">
        <p class="holder-name">Miles Vetcher</p>
        <p class="holder-title">Licensed Real Estate Broker</p>
      </div>
      <address class="address" style="font-style: normal;">
        2385 West 9th Avenue<br>
        Brooklyn, NY 11230
      </address>
      <div class="contact">
        <p>Phone: 718-555-0142<span class="sep">|</span>Cell: 917-555-0187</p>
        <p>Fax: 866-555-0163<span class="sep">|</span>Email: brookgaterealtyny@quorvana.com</p>
        <p>www.bgrny.com</p>
      </div>
    </section>

    <section class="card card-back">
      <div class="back-brand">
        <span class="back-square"></span>
        <span class="back-name">Brook Gate Realty</span>
      </div>
    </section>
  </main>
</body>
</html>
```